Business Card Design for general contractor or developer

General Contractors. We build new buildings as well as redesign and/or remodel existing buildings. Mostly residential, but we want to expand to commercial as well, so we want the design not to be residential specific.We want the design to be modern, but necessarily minimalistic. A monogram type is also a consideration, but would like to see all ideas.

Target Market(s)

Real estate investors, homeowners, future homeowners, commercial building owners

Industry/Entity Type

Contractor

Contact Information for Business Card

BRIMCOVE Developers Corp, 2917 NE 88th Avenue Suite 412 Coral Springs, FL 33071, Darren Kopec, (305) 555-0148, darren@brimcovedev.example

Font styles to use
Other font styles liked:
• Modern type font

Requirements
Must have
• Must be modern looking
Nice to have
• Metallic type or a standout feature
Should not have
• Tools, floorplans

```html
<!DOCTYPE html>
<html lang="en">
<head>
<meta charset="utf-8">
<title>Brimcove Developers Corp — Business Card Presentation</title>
<link rel="stylesheet" href="https://fonts.googleapis.com/css2?family=Questrial&display=swap">
<style>
  :root {
    --board: #fce6ad;
    --sky-top: #e4f0fb;
    --sky-bottom: #8db3ef;
    --card-blue: #8fb6f2;
    --card-white: #ffffff;
    --ink-blue: #6f95d8;
    --ink-white: #ffffff;
    --ink-dark: #1c1c1c;
    --shadow: rgba(40, 30, 10, 0.55);
  }
  * { box-sizing: border-box; margin: 0; padding: 0; }
  html, body {
    width: 849px;
    height: 1200px;
    overflow: hidden;
    background: var(--board);
    font-family: "Questrial", sans-serif;
  }
  .board { position: relative; width: 849px; height: 1200px; }

  .card {
    position: absolute;
    box-shadow: 6px 6px 4px var(--shadow);
  }
  .card--portrait { top: 42px; width: 278px; height: 468px; }
  .card--landscape { left: 42px; width: 462px; height: 271px; background: var(--card-blue); }

  .front-portrait {
    left: 42px;
    background: linear-gradient(180deg, var(--sky-top) 0%, #c2d8f6 45%, var(--sky-bottom) 100%);
  }
  .back-portrait { left: 357px; background: var(--card-white); color: var(--ink-blue); }
  .front-landscape { top: 572px; }
  .back-landscape { top: 872px; color: var(--ink-white); }

  .wordmark {
    position: absolute;
    text-align: center;
    line-height: 1;
    letter-spacing: 3px;
  }
  .wordmark__name { display: block; font-size: 52px; letter-spacing: 1px; }
  .wordmark__sub { display: block; margin-top: 8px; font-size: 19px; letter-spacing: 5px; }

  .front-portrait .wordmark { left: 0; right: 0; top: 270px; color: var(--ink-white); }
  .front-portrait .wordmark__name { font-size: 48px; }
  .front-portrait .wordmark__sub { font-size: 17px; letter-spacing: 4px; }

  .front-landscape .wordmark { left: 0; right: 0; top: 98px; color: var(--ink-white); }

  .contact-name { font-size: 17px; letter-spacing: 2px; }
  .contact-lines { font-size: 14px; letter-spacing: 2px; line-height: 1.45; }

  .back-portrait .contact-name { position: absolute; left: 34px; top: 310px; }
  .back-portrait .address { position: absolute; left: 34px; top: 370px; }
  .back-portrait .reach { position: absolute; left: 34px; top: 458px; }
  .back-portrait .reach { top: auto; bottom: 16px; font-size: 13px; }
  .back-portrait .address { top: 286px; }
  .back-portrait .contact-name { top: 226px; }

  .back-landscape .contact-name { position: absolute; left: 14px; top: 100px; font-size: 19px; }
  .back-landscape .reach { position: absolute; left: 14px; top: 148px; }
  .back-landscape .address { position: absolute; left: 14px; top: 218px; }

  .standalone { position: absolute; left: 580px; width: 250px; color: var(--ink-dark); text-align: center; }
  .standalone--stacked { top: 660px; }
  .standalone--stacked .wordmark__name { font-size: 50px; }
  .standalone--stacked .wordmark__sub { font-size: 18px; letter-spacing: 3px; }
  .standalone--wide { top: 880px; }
  .standalone--wide .wordmark__name { font-size: 50px; }
  .standalone--wide .wordmark__sub { font-size: 18px; letter-spacing: 5px; margin-top: 14px; }
  .standalone .wordmark { position: static; }
</style>
</head>
<body>
<main class="board">

  <section class="card card--portrait front-portrait">
    <div class="wordmark">
      <span class="wordmark__name">BRIMCOVE</span>
      <span class="wordmark__sub">DEVELOPERS CORP.</span>
    </div>
  </section>

  <section class="card card--portrait back-portrait">
    <p class="contact-name">Darren Kopec</p>
    <p class="contact-lines address">2917 NE 88th<br>Avenue<br>Suite 412<br>Coral Springs<br>FL 33071</p>
    <p class="contact-lines reach">(305) 555-0148<br>darren@brimcovedev.example</p>
  </section>

  <section class="card card--landscape front-landscape">
    <div class="wordmark">
      <span class="wordmark__name">BRIMCOVE</span>
      <span class="wordmark__sub">DEVELOPERS CORP.</span>
    </div>
  </section>

  <section class="card card--landscape back-landscape">
    <p class="contact-name">Darren Kopec</p>
    <p class="contact-lines reach">(305) 555-0148<br>darren@brimcovedev.example</p>
    <p class="contact-lines address">2917 NE 88th Avenue Suite 412<br>Coral Springs FL 33071</p>
  </section>

  <aside class="standalone standalone--stacked">
    <div class="wordmark">
      <span class="wordmark__name">BRIMCOVE</span>
      <span class="wordmark__sub">DEVELOPERS CORP.</span>
    </div>
  </aside>

  <aside class="standalone standalone--wide">
    <div class="wordmark">
      <span class="wordmark__name">BRIMCOVE</span>
      <span class="wordmark__sub">DEVELOPERS CORP.</span>
    </div>
  </aside>

</main>
</body>
</html>
```